Interval Timer App

Need to have design for the attached wireframe. Similar app can be found here: https://shop.vantrelapps.net/store/apps/details?id=cc.brimlowe.intervaltimer

```html
<!DOCTYPE html>
<html lang="en">
<head>
<meta charset="utf-8">
<title>Interval Timer App</title>
<link href="https://fonts.googleapis.com/css2?family=Roboto:wght@100;300;400;500;700&display=swap" rel="stylesheet">
<style>
  :root {
    --red: #ef5356;
    --green: #3bdea8;
    --blue: #2759f0;
    --grey-band: #e3e3e3;
    --ink: #1d1d1d;
    --muted: #a9a9a9;
    --white: #ffffff;
    --teal: #3ccfb4;
    --lime: #86c540;
    --amber: #fbb308;
    --orange: #f57a3a;
    --notif-blue: #3b6fe0;
  }
  * { box-sizing: border-box; margin: 0; padding: 0; }
  html, body { width: 1200px; height: 768px; overflow: hidden; background: var(--white); }
  body { position: relative; font-family: "Roboto", Arial, sans-serif; }

  .deco { position: absolute; }
  .deco--green-dot { left: -54px; top: -22px; width: 140px; height: 140px; border-radius: 50%; background: var(--green); }
  .deco--red-pill-top { left: 764px; top: -8px; width: 520px; height: 138px; border-radius: 69px; background: var(--red); }
  .deco--grey-band { left: 830px; top: 328px; width: 370px; height: 141px; background: var(--grey-band); }
  .deco--grey-pill { left: -200px; top: 659px; width: 456px; height: 200px; border-radius: 100px; background: var(--grey-band); }
  .deco--red-pill { left: 306px; top: 666px; width: 211px; height: 200px; border-radius: 100px; background: var(--red); }
  .deco--green-pill { left: 960px; top: 659px; width: 400px; height: 200px; border-radius: 100px; background: var(--green); }

  .screen {
    position: absolute; width: 218px; height: 386px; overflow: hidden;
    box-shadow: 0 10px 30px rgba(0,0,0,0.12);
  }
  .screen--lock { left: 116px; top: 208px; background: radial-gradient(ellipse at 45% 45%, #6a6a6a 0%, #4c4c4c 55%, #3d3d3d 100%); }
  .screen--setup { left: 366px; top: 212px; background: var(--white); }
  .screen--rest { left: 612px; top: 214px; background: var(--red); color: var(--white); }
  .screen--work { left: 859px; top: 212px; background: var(--green); color: var(--white); }

  .status-bar { position: absolute; left: 0; top: 0; width: 100%; height: 12px; font-size: 6px; display: flex; align-items: center; justify-content: space-between; padding: 0 4px; }
  .status-bar__time { position: absolute; left: 50%; transform: translateX(-50%); }
  .status-bar__right { display: flex; align-items: center; gap: 2px; }
  .screen--setup .status-bar { color: var(--ink); }
  .screen--rest .status-bar, .screen--work .status-bar { color: rgba(255,255,255,0.85); }

  /* lock screen */
  .lock__time { position: absolute; width: 100%; top: 64px; text-align: center; color: var(--white); font-weight: 100; font-size: 38px; }
  .lock__date { position: absolute; width: 100%; top: 110px; text-align: center; color: var(--white); font-size: 8.5px; }
  .notif { position: absolute; left: 3px; width: 212px; height: 41px; background: var(--white); border-radius: 2px; }
  .notif--timer { top: 146px; }
  .notif--social { top: 190px; }
  .notif__icon { position: absolute; left: 14px; top: 9px; width: 23px; height: 23px; border-radius: 50%; }
  .notif--timer .notif__icon { background: var(--red); display: flex; align-items: center; justify-content: center; }
  .notif--social .notif__icon { background: var(--notif-blue); }
  .notif__clock { position: absolute; left: 47px; top: 12px; color: var(--red); font-weight: 300; font-size: 13px; }
  .notif__label { position: absolute; left: 108px; top: 16px; color: var(--red); font-weight: 700; font-size: 7.5px; letter-spacing: 0.8px; }
  .notif__btn { position: absolute; top: 12px; width: 17px; height: 17px; border-radius: 50%; display: flex; align-items: center; justify-content: center; }
  .notif__btn--play { left: 161px; background: var(--red); }
  .notif__btn--pause { left: 185px; background: var(--white); box-shadow: 0 1px 4px rgba(0,0,0,0.2); }
  .notif__app { position: absolute; left: 47px; top: 10px; color: var(--notif-blue); font-weight: 500; font-size: 8.5px; }
  .notif__text { position: absolute; left: 47px; top: 22px; color: #8a8a8a; font-size: 7.5px; }
  .notif__stamp { position: absolute; right: 14px; top: 11px; color: #555; font-size: 6px; }
  .lock__hint { position: absolute; width: 100%; top: 333px; text-align: center; color: var(--white); font-size: 8.5px; }

  /* setup screen */
  .modes { position: absolute; top: 26px; left: 36px; display: flex; gap: 6px; align-items: center; }
  .mode { width: 23px; height: 23px; border-radius: 50%; display: flex; align-items: center; justify-content: center; }
  .mode--message { background: var(--teal); }
  .mode--sound { background: var(--lime); }
  .mode--light { background: var(--amber); }
  .mode--vibrate { background: var(--orange); }
  .mode--timer { background: var(--red); }
  .settings-gear { margin-left: 6px; }
  .field { position: absolute; left: 0; width: 100%; }
  .field__label { text-align: center; color: var(--muted); font-size: 7px; letter-spacing: 2px; font-weight: 500; }
  .field__row { position: relative; height: 46px; }
  .field__value { position: absolute; left: 50%; top: 50%; transform: translate(-50%,-50%); color: var(--ink); font-weight: 100; font-size: 40px; }
  .field__step { position: absolute; top: 50%; transform: translate(-50%,-50%); color: #bdbdbd; font-weight: 300; font-size: 16px; }
  .field__step--plus { left: 51px; }
  .field__step--minus { left: 170px; }
  .field--sets { top: 74px; }
  .field--work { top: 161px; }
  .field--rest { top: 248px; }
  .fab { position: absolute; left: 164px; top: 334px; width: 37px; height: 37px; border-radius: 50%; display: flex; align-items: center; justify-content: center; box-shadow: 0 3px 8px rgba(0,0,0,0.25); }
  .fab--start { background: var(--blue); }
  .fab--pause { background: var(--white); }

  /* run screens */
  .sets { position: absolute; right: 28px; top: 34px; display: flex; align-items: center; gap: 12px; }
  .sets__label { font-size: 7.5px; font-weight: 700; letter-spacing: 2px; }
  .sets__count { font-size: 26px; font-weight: 300; }
  .run__clock { position: absolute; width: 100%; top: 168px; text-align: center; font-weight: 100; font-size: 42px; }
  .run__phase { position: absolute; width: 100%; top: 248px; text-align: center; font-weight: 300; font-size: 28px; }
</style>
</head>
<body>
  <div class="deco deco--green-dot"></div>
  <div class="deco deco--red-pill-top"></div>
  <div class="deco deco--grey-band"></div>
  <div class="deco deco--grey-pill"></div>
  <div class="deco deco--red-pill"></div>
  <div class="deco deco--green-pill"></div>

  <!-- lock screen -->
  <section class="screen screen--lock">
    <div class="lock__time">9:41</div>
    <div class="lock__date">Tuesday, Sept 25</div>
    <div class="notif notif--timer">
      <div class="notif__icon">
        <svg width="13" height="13" viewBox="0 0 14 14"><circle cx="7" cy="8" r="5" fill="none" stroke="#fff" stroke-width="1.4"/><path d="M7 5v3.2M5.5 1.5h3" stroke="#fff" stroke-width="1.4" stroke-linecap="round"/></svg>
      </div>
      <div class="notif__clock">00:05</div>
      <div class="notif__label">WORK: 5</div>
      <div class="notif__btn notif__btn--play"><svg width="6" height="6" viewBox="0 0 6 6"><path d="M1 0.5L5.5 3 1 5.5z" fill="#fff"/></svg></div>
      <div class="notif__btn notif__btn--pause"><svg width="5" height="5" viewBox="0 0 5 5"><rect x="0.5" width="1.3" height="5" fill="#ef5356"/><rect x="3.2" width="1.3" height="5" fill="#ef5356"/></svg></div>
    </div>
    <div class="notif notif--social">
      <div class="notif__icon"></div>
      <div class="notif__app">Pinloop</div>
      <div class="notif__text">Commented on your photo</div>
      <div class="notif__stamp">8:12PM</div>
    </div>
    <div class="lock__hint">Swipe to unlock</div>
  </section>

  <!-- setup screen -->
  <section class="screen screen--setup">
    <div class="status-bar">
      <svg width="14" height="6" viewBox="0 0 14 6"><rect x="0" y="4" width="1.5" height="2" fill="currentColor"/><rect x="2.2" y="3" width="1.5" height="3" fill="currentColor"/><rect x="4.4" y="2" width="1.5" height="4" fill="currentColor"/><rect x="6.6" y="1" width="1.5" height="5" fill="currentColor"/><path d="M9.5 2.5a3.5 3.5 0 0 1 4 0M10.4 3.8a2 2 0 0 1 2.2 0" stroke="currentColor" stroke-width="0.8" fill="none"/></svg>
      <span class="status-bar__time">9:41 AM</span>
      <span class="status-bar__right">&#8727; 100% <svg width="14" height="6" viewBox="0 0 14 6"><rect x="0.3" y="0.3" width="12" height="5.4" rx="1" fill="none" stroke="currentColor" stroke-width="0.6"/><rect x="1" y="1" width="10.6" height="4" fill="currentColor"/><rect x="12.6" y="2" width="1" height="2" fill="currentColor"/></svg></span>
    </div>
    <div class="modes">
      <div class="mode mode--message"><svg width="10" height="10" viewBox="0 0 10 10"><rect x="1" y="1.5" width="8" height="6" rx="1" fill="#fff"/><path d="M3 7.5L3 9.5 5 7.5z" fill="#fff"/></svg></div>
      <div class="mode mode--sound"><svg width="11" height="10" viewBox="0 0 11 10"><path d="M1 3.5h2l3-2.5v8l-3-2.5H1z" fill="#fff"/><path d="M7.5 3a2.5 2.5 0 0 1 0 4M8.8 1.8a4 4 0 0 1 0 6.4" stroke="#fff" stroke-width="0.9" fill="none"/></svg></div>
      <div class="mode mode--light"><svg width="10" height="11" viewBox="0 0 10 11"><circle cx="5" cy="4.2" r="3.3" fill="none" stroke="#fff" stroke-width="1.2"/><rect x="3.5" y="8" width="3" height="2" fill="#fff"/></svg></div>
      <div class="mode mode--vibrate"><svg width="12" height="10" viewBox="0 0 12 10"><rect x="3.5" y="1" width="5" height="8" rx="0.8" fill="none" stroke="#fff" stroke-width="1.1"/><path d="M1.5 3v4M10.5 3v4" stroke="#fff" stroke-width="1"/></svg></div>
      <div class="mode mode--timer"><svg width="11" height="11" viewBox="0 0 14 14"><circle cx="7" cy="8" r="5" fill="none" stroke="#fff" stroke-width="1.4"/><path d="M7 5v3.2M5.5 1.5h3" stroke="#fff" stroke-width="1.4" stroke-linecap="round"/></svg></div>
      <svg class="settings-gear" width="10" height="10" viewBox="0 0 10 10"><circle cx="5" cy="5" r="3" fill="none" stroke="#1d1d1d" stroke-width="1.8" stroke-dasharray="1.6 0.8"/><circle cx="5" cy="5" r="2.4" fill="#1d1d1d"/><circle cx="5" cy="5" r="1" fill="#fff"/></svg>
    </div>

    <div class="field field--sets">
      <div class="field__label">SETS</div>
      <div class="field__row"><span class="field__step field__step--plus">+</span><span class="field__value">5</span><span class="field__step field__step--minus">&minus;</span></div>
    </div>
    <div class="field field--work">
      <div class="field__label">WORK</div>
      <div class="field__row"><span class="field__step field__step--plus">+</span><span class="field__value">2:50</span><span class="field__step field__step--minus">&minus;</span></div>
    </div>
    <div class="field field--rest">
      <div class="field__label">REST</div>
      <div class="field__row"><span class="field__step field__step--plus">+</span><span class="field__value">1:45</span><span class="field__step field__step--minus">&minus;</span></div>
    </div>
    <div class="fab fab--start"><svg width="10" height="11" viewBox="0 0 10 11"><path d="M1.5 0.5L9.5 5.5 1.5 10.5z" fill="#fff"/></svg></div>
  </section>

  <!-- rest screen -->
  <section class="screen screen--rest">
    <div class="status-bar">
      <svg width="14" height="6" viewBox="0 0 14 6"><rect x="0" y="4" width="1.5" height="2" fill="currentColor"/><rect x="2.2" y="3" width="1.5" height="3" fill="currentColor"/><rect x="4.4" y="2" width="1.5" height="4" fill="currentColor"/><rect x="6.6" y="1" width="1.5" height="5" fill="currentColor"/><path d="M9.5 2.5a3.5 3.5 0 0 1 4 0M10.4 3.8a2 2 0 0 1 2.2 0" stroke="currentColor" stroke-width="0.8" fill="none"/></svg>
      <span class="status-bar__time">9:41 AM</span>
      <span class="status-bar__right">&#8727; 100% <svg width="14" height="6" viewBox="0 0 14 6"><rect x="0.3" y="0.3" width="12" height="5.4" rx="1" fill="none" stroke="currentColor" stroke-width="0.6"/><rect x="1" y="1" width="10.6" height="4" fill="currentColor"/><rect x="12.6" y="2" width="1" height="2" fill="currentColor"/></svg></span>
    </div>
    <div class="sets"><span class="sets__label">SETS</span><span class="sets__count">5</span></div>
    <div class="run__clock">00:05</div>
    <div class="run__phase">Rest</div>
    <div class="fab fab--pause"><svg width="8" height="9" viewBox="0 0 8 9"><rect x="0.5" width="2.4" height="9" fill="#ef5356"/><rect x="5.1" width="2.4" height="9" fill="#ef5356"/></svg></div>
  </section>

  <!-- work screen -->
  <section class="screen screen--work">
    <div class="status-bar">
      <svg width="14" height="6" viewBox="0 0 14 6"><rect x="0" y="4" width="1.5" height="2" fill="currentColor"/><rect x="2.2" y="3" width="1.5" height="3" fill="currentColor"/><rect x="4.4" y="2" width="1.5" height="4" fill="currentColor"/><rect x="6.6" y="1" width="1.5" height="5" fill="currentColor"/><path d="M9.5 2.5a3.5 3.5 0 0 1 4 0M10.4 3.8a2 2 0 0 1 2.2 0" stroke="currentColor" stroke-width="0.8" fill="none"/></svg>
      <span class="status-bar__time">9:41 AM</span>
      <span class="status-bar__right">&#8727; 100% <svg width="14" height="6" viewBox="0 0 14 6"><rect x="0.3" y="0.3" width="12" height="5.4" rx="1" fill="none" stroke="currentColor" stroke-width="0.6"/><rect x="1" y="1" width="10.6" height="4" fill="currentColor"/><rect x="12.6" y="2" width="1" height="2" fill="currentColor"/></svg></span>
    </div>
    <div class="sets"><span class="sets__label">SETS</span><span class="sets__count">5</span></div>
    <div class="run__clock">00:05</div>
    <div class="run__phase">Work</div>
    <div class="fab fab--pause"><svg width="8" height="9" viewBox="0 0 8 9"><rect x="0.5" width="2.4" height="9" fill="#3bdea8"/><rect x="5.1" width="2.4" height="9" fill="#3bdea8"/></svg></div>
  </section>
</body>
</html>
```